Modern Business Card For A Digital Advertising Company

I'll be print on the Tarn Prints Velour paper http://us.tarnprints.example/products/velour/business-cards.html
Need's to be modern and use the color palette of the logo or gray scales. I think integrating the pixelation of the logo in to the card and having it wrap from one side to the other could be interesting. My company provides ad operations, web development, and number of other services to websites around the world. You can see my website at http://www.pixelharbor.example
Contact info on the card needs to have
Dana Welloby
President
p.555.318.4406
dana@pixelharbor.example
http://www.pixelharbor.example
Doesn't necessarily need to be in that order
Target Market(s)
Website owners
Industry/Entity Type
Business
Look and feel

```html
<!DOCTYPE html>
<html lang="en">
<head>
<meta charset="utf-8">
<title>Pixel Harbor – Business Card</title>
<link rel="stylesheet" href="https://fonts.googleapis.com/css2?family=Source+Sans+3:wght@400;600&display=swap">
<style>
  :root {
    --stage: #f1f1ef;
    --card: #e8eae7;
    --band: #696a6c;
    --band-shadow: rgba(0,0,0,0.28);
    --panel: #8f9091;
    --panel-edge: #7d7e80;
    --green: #8cc63f;
    --white: #ffffff;
    --label: #eeeeee;
  }
  * { box-sizing: border-box; margin: 0; padding: 0; }
  html, body {
    width: 1200px; height: 1000px; overflow: hidden;
    background: var(--stage);
    font-family: "Source Sans 3", "Myriad Pro", sans-serif;
  }
  .canvas { position: relative; width: 1200px; height: 1000px; }

  .card {
    position: absolute; width: 620px; height: 360px;
    background: var(--card); overflow: hidden;
    box-shadow: 0 6px 18px rgba(0,0,0,0.18);
  }
  .card--front { left: 130px; top: 100px; }
  .card--back  { left: 450px; top: 540px; }

  .band {
    position: absolute; background: var(--band);
    box-shadow: 0 6px 10px var(--band-shadow);
  }
  .pixel-strip { position: absolute; background: var(--green); }

  /* front face */
  .card--front .band { left: 0; top: 85px; width: 520px; height: 220px; }
  .card--front .band-tab { position: absolute; left: 0; top: 92px; width: 510px; height: 210px; background: #717274; }
  .card--front .pixel-strip { left: 0; top: 98px; width: 140px; height: 44px; }
  .brand {
    position: absolute; left: 200px; top: 175px;
    display: flex; align-items: center; gap: 12px;
  }
  .brand-mark { width: 26px; height: 26px; background: var(--green); }
  .brand-name {
    font-weight: 600; font-size: 32px; letter-spacing: 1px;
    color: var(--green);
  }

  /* back face */
  .card--back .band { left: 0; top: 40px; width: 500px; height: 275px; }
  .card--back .pixel-strip--top { left: 0; top: 50px; width: 490px; height: 44px; }
  .card--back .pixel-strip--wrap { left: 500px; top: 200px; width: 120px; height: 44px; }
  .info-panel {
    position: absolute; left: 0; top: 130px; width: 290px; height: 120px;
    background: var(--panel); box-shadow: 0 4px 8px var(--band-shadow);
  }
  .info-panel-tab {
    position: absolute; left: 0; top: 140px; width: 300px; height: 120px;
    background: var(--panel-edge);
  }
  .contact { position: absolute; left: 16px; top: 142px; list-style: none; }
  .contact li { display: flex; align-items: baseline; height: 30px; }
  .contact .label { width: 54px; font-size: 12px; color: var(--label); }
  .contact .value { font-size: 17px; color: var(--white); }
  .person { position: absolute; left: 300px; top: 218px; text-align: right; width: 190px; color: var(--white); }
  .person-name { font-size: 34px; line-height: 1; text-shadow: 0 2px 3px rgba(0,0,0,0.4); white-space: nowrap; }
  .person-title { font-size: 16px; margin-top: 2px; padding-right: 40px; }
</style>
</head>
<body>
<main class="canvas">

  <section class="card card--front" aria-label="Card front">
    <div class="band"></div>
    <div class="band-tab"></div>
    <div class="pixel-strip" role="img" aria-label="Green pixel pattern strip"></div>
    <div class="brand">
      <span class="brand-mark"></span>
      <span class="brand-name">PIXEL HARBOR</span>
    </div>
  </section>

  <section class="card card--back" aria-label="Card back">
    <div class="band"></div>
    <div class="pixel-strip pixel-strip--top" role="img" aria-label="Green pixel pattern strip"></div>
    <div class="pixel-strip pixel-strip--wrap" role="img" aria-label="Green pixel pattern strip wrapping off the edge"></div>
    <div class="info-panel-tab"></div>
    <div class="info-panel"></div>
    <ul class="contact">
      <li><span class="label">Phone:</span><span class="value">555.318.4406</span></li>
      <li><span class="label">Web:</span><span class="value">www.pixelharbor.example</span></li>
      <li><span class="label">Email:</span><span class="value">dana@pixelharbor.example</span></li>
    </ul>
    <div class="person">
      <div class="person-name">Dana Welloby</div>
      <div class="person-title">President</div>
    </div>
  </section>

</main>
</body>
</html>
```